Equestrian brand 'health check' webinar template

I am looking to host a series of webinars promoting my consulting business in equestrian business development. I work mainly with start-ups and young brands looking to establish their brand in the international equestrian marketplace mainly focussed on horse riding fashion and horse riding essentials.
The topic of the webinar is a 'brand health check': helping brands understand what they really stand for if they are really 'talking' to the right audience and delivering the right message. Additionally, we'll touch on having all the brand fundamentals in place to become successful.
I am looking for a webinar/presentation template that is professional and shows off the topics in the best possible way, in keeping with the equestrian theme and the current look and feel of the website: thecopperlanternadvisorygroup.com
Target Market(s)
Equestrian businesses, start-up, fashion
Industry/Entity Type
Business
Logo Text
conceptual high market equestrian services style
Colors

```html
<!DOCTYPE html>
<html lang="en">
<head>
<meta charset="utf-8">
<title>Brand Health Check – Webinar Template</title>
<link rel="stylesheet" href="https://fonts.googleapis.com/css2?family=Raleway:wght@300;600;700;800&family=Roboto+Slab:wght@300;400;600&display=swap">
<style>
  :root {
    --canvas: #dcdde0;
    --white: #ffffff;
    --lilac: #b794b6;
    --lilac-soft: #c9a9c8;
    --plum: #7a4f7c;
    --plum-deep: #8a5c8a;
    --heading: #a67fa6;
    --ink: #2e2a2e;
    --photo-dark: #3a3a3a;
    --photo-green: #2f4a2c;
  }
  html, body { margin: 0; padding: 0; overflow: hidden; }
  body { width: 1200px; height: 1200px; background: var(--canvas); }
  .sheet { display: block; width: 1200px; height: 1200px; }
  .slide { filter: drop-shadow(0 3px 4px rgba(0,0,0,.22)); }
  .display { font-family: 'Raleway', sans-serif; font-weight: 700; }
  .display-light { font-family: 'Raleway', sans-serif; font-weight: 300; }
  .body { font-family: 'Roboto Slab', serif; font-weight: 300; font-size: 11px; fill: var(--ink); }
  .body-light { font-family: 'Roboto Slab', serif; font-weight: 300; font-size: 11px; fill: var(--white); }
  .quote { font-family: 'Roboto Slab', serif; font-weight: 300; font-size: 19px; fill: var(--white); }
  .icon { fill: none; stroke: var(--lilac); stroke-width: 2.5; stroke-linecap: round; stroke-linejoin: round; }
</style>
</head>
<body>
<svg class="sheet" viewBox="0 0 1500 1500" xmlns="http://www.w3.org/2000/svg">

  <!-- Slide: agenda with icons -->
  <g class="slide">
    <rect x="70" y="104" width="664" height="374" fill="var(--white)"/>
    <polygon points="70,104 390,104 310,478 70,478" fill="var(--photo-dark)" role="img" aria-label="Black and white photo of a rider on a horse"/>
    <polygon points="390,104 394,104 314,478 310,478" fill="var(--lilac)"/>
    <rect x="70" y="145" width="12" height="56" fill="var(--lilac)"/>
    <text class="display" x="93" y="168" font-size="29" fill="var(--white)">LOREM IPSUM</text>
    <text class="display" x="93" y="197" font-size="29" fill="var(--white)">SIT AMET</text>

    <g>
      <circle cx="373" cy="176" r="32" fill="var(--white)" stroke="var(--lilac)" stroke-width="3"/>
      <path class="icon" d="M360 172 h6 l16 -10 v26 l-16 -10 h-6 z M364 182 l3 9"/>
      <text class="display" x="421" y="158" font-size="17" fill="var(--heading)" font-weight="600">LOREM IPSUM DOLOR</text>
      <text class="body" x="419" y="173">Lorem ipsum dolor sit amet, consectetuer Lorem ipsum</text>
      <text class="body" x="419" y="188">dolor sit amet, consectetuer adipiscing elit, sed diam</text>
      <text class="body" x="419" y="203">nonummy nibh euismod tincidunt ut laoreet</text>
    </g>
    <g>
      <circle cx="348" cy="290" r="32" fill="var(--white)" stroke="var(--lilac)" stroke-width="3"/>
      <path class="icon" d="M338 278 h20 v6 a10 10 0 0 1 -20 0 z M338 281 h-5 a5 5 0 0 0 6 7 M358 281 h5 a5 5 0 0 1 -6 7 M348 294 v6 M341 304 h14"/>
      <text class="display" x="396" y="272" font-size="17" fill="var(--heading)" font-weight="600">LOREM IPSUM DOLOR</text>
      <text class="body" x="394" y="287">Lorem ipsum dolor sit amet, consectetuer Lorem ipsum</text>
      <text class="body" x="394" y="302">dolor sit amet, consectetuer adipiscing elit, sed diam</text>
      <text class="body" x="394" y="317">nonummy nibh euismod tincidunt ut laoreet</text>
    </g>
    <g>
      <circle cx="325" cy="405" r="32" fill="var(--white)" stroke="var(--lilac)" stroke-width="3"/>
      <path class="icon" d="M337 392 c-10 0 -18 8 -20 18 l5 5 c10 -2 18 -10 18 -20 z M318 404 l-5 1 -2 5 5 -1 M326 414 l-1 5 5 -2 1 -5"/>
      <text class="display" x="373" y="386" font-size="17" fill="var(--heading)" font-weight="600">LOREM IPSUM DOLOR</text>
      <text class="body" x="373" y="401">Lorem ipsum dolor sit amet, consectetuer Lorem ipsum</text>
      <text class="body" x="373" y="416">dolor sit amet, consectetuer adipiscing elit, sed diam</text>
      <text class="body" x="373" y="431">nonummy nibh euismod tincidunt ut laoreet</text>
    </g>
  </g>

  <!-- Slide: key figures over photo -->
  <g class="slide">
    <defs>
      <linearGradient id="jump-photo" x1="0" y1="0" x2="0" y2="1">
        <stop offset="0" stop-color="var(--photo-green)"/>
        <stop offset="0.7" stop-color="#3b4a36"/>
        <stop offset="1" stop-color="#5a5048"/>
      </linearGradient>
    </defs>
    <rect x="784" y="104" width="664" height="374" fill="url(#jump-photo)" role="img" aria-label="Photo of a rider show jumping a horse in front of trees"/>
    <circle cx="946" cy="268" r="110" fill="var(--lilac)" opacity="0.88"/>
    <text class="display" x="946" y="263" font-size="60" fill="var(--white)" text-anchor="middle">82%</text>
    <text class="body-light" x="946" y="289" text-anchor="middle">Lorem ipsum dolor sit amet,</text>
    <text class="body-light" x="946" y="304" text-anchor="middle">consectetuer Lorem ipsum dolor sit</text>
    <text class="body-light" x="946" y="319" text-anchor="middle">amet, consectetuer adipiscing elit.</text>
    <circle cx="1304" cy="383" r="73" fill="var(--plum-deep)" opacity="0.92"/>
    <text class="display" x="1304" y="387" font-size="48" fill="var(--white)" text-anchor="middle">30%</text>
    <text class="body-light" x="1304" y="405" text-anchor="middle">Lorem ipsum dolor sit</text>
    <text class="body-light" x="1304" y="420" text-anchor="middle">amet, consectetuer.</text>
  </g>

  <!-- Slide: mission and vision -->
  <g class="slide">
    <rect x="70" y="565" width="664" height="188" fill="var(--white)"/>
    <rect x="70" y="752" width="664" height="187" fill="var(--lilac)"/>
    <text class="display" x="401" y="624" font-size="26" fill="var(--heading)" text-anchor="middle">OUR MISSION</text>
    <g class="body" text-anchor="middle">
      <text x="401" y="649">Lorem ipsum dolor sit amet, consectetuer Lorem ipsum dolor sit amet,</text>
      <text x="401" y="664">consectetuer adipiscing elit, sed diam nonummy nibh euismod tincidunt ut</text>
      <text x="401" y="679">laoreet Lorem ipsum dolor sit amet, consectetuer adipiscing elit, sed diam</text>
      <text x="401" y="694">nonummy nibh euismod tincidunt ut laoreet dolore magna aliquam erat</text>
      <text x="401" y="708">volutpat. Ut wisi enim ad minim veniam, quis nostrud exerci tation ullamcorper</text>
      <text x="401" y="723">suscipit lobortis nisl ut aliquip ex ea commodo consequat.</text>
    </g>
    <text class="display" x="401" y="806" font-size="26" fill="var(--white)" text-anchor="middle">OUR VISION</text>
    <g class="body-light" text-anchor="middle" opacity="0.9">
      <text x="401" y="831">Lorem ipsum dolor sit amet, consectetuer Lorem ipsum dolor sit amet,</text>
      <text x="401" y="846">consectetuer adipiscing elit, sed diam nonummy nibh euismod tincidunt ut</text>
      <text x="401" y="861">laoreet Lorem ipsum dolor sit amet, consectetuer adipiscing elit, sed diam</text>
      <text x="401" y="875">nonummy nibh euismod tincidunt ut laoreet dolore magna aliquam erat</text>
      <text x="401" y="890">volutpat.</text>
    </g>
  </g>

  <!-- Slide: list with bullets -->
  <g class="slide">
    <rect x="784" y="564" width="665" height="374" fill="var(--white)"/>
    <text class="display" x="819" y="634" font-size="28" fill="var(--heading)" font-weight="600">LOREM IPSUM SIT AMET</text>
    <g class="body">
      <text x="819" y="664">Lorem ipsum dolor sit amet, consectetuer Lorem ipsum dolor sit amet, consectetuer adipiscing elit, sed diam nonummy</text>
      <text x="819" y="678">nibh euismod tincidunt ut laoreet Lorem ipsum dolor sit amet, consectetuer adipiscing elit, sed diam nonummy nibh</text>
      <text x="819" y="693">euismod tincidunt ut laoreet dolore magna aliquam erat volutpat. Ut wisi enim ad minim veniam, quis nostrud exerci</text>
      <text x="819" y="708">tation ullamcorper suscipit lobortis nisl ut aliquip ex ea commodo consequat.</text>
    </g>
    <g fill="var(--lilac)">
      <circle cx="836" cy="751" r="19"/>
      <circle cx="836" cy="809" r="19"/>
      <circle cx="836" cy="868" r="19"/>
      <circle cx="1135" cy="751" r="19"/>
      <circle cx="1135" cy="809" r="19"/>
    </g>
    <g class="body">
      <text x="864" y="747">Lorem Lorem ipsum dolor sit amet,</text>
      <text x="864" y="762">consectetuer adipiscing elit, sed diam</text>
      <text x="864" y="805">Lorem Lorem ipsum dolor sit amet,</text>
      <text x="864" y="820">consectetuer adipiscing elit, sed diam</text>
      <text x="864" y="864">Lorem Lorem ipsum dolor sit amet,</text>
      <text x="864" y="879">consectetuer adipiscing elit, sed diam</text>
      <text x="1163" y="747">Lorem Lorem ipsum dolor sit amet,</text>
      <text x="1163" y="762">consectetuer adipiscing elit, sed diam</text>
      <text x="1163" y="805">Lorem Lorem ipsum dolor sit amet,</text>
      <text x="1163" y="820">consectetuer adipiscing elit, sed diam</text>
    </g>
  </g>

  <!-- Slide: testimonial -->
  <g class="slide">
    <rect x="70" y="1023" width="664" height="374" fill="var(--lilac)"/>
    <rect x="70" y="1127" width="664" height="165" fill="var(--plum)"/>
    <text class="quote" x="122" y="1195">“Thank you The Copper Lantern Advisory Group for your</text>
    <text class="quote" x="122" y="1218">creative thinking, professionalism and super efficient</text>
    <text class="quote" x="122" y="1242">service. You are a dream to work with.”</text>
    <text x="555" y="1323" text-anchor="end" font-family="'Roboto Slab', serif" font-weight="600" font-size="17" fill="var(--white)">HELENA MARWICK</text>
    <text x="555" y="1344" text-anchor="end" font-family="'Roboto Slab', serif" font-weight="300" font-size="14" fill="var(--white)">CEO BRIGHTVALE</text>
    <circle cx="629" cy="1297" r="61" fill="var(--white)"/>
    <text x="629" y="1302" text-anchor="middle" font-family="'Raleway', sans-serif" font-weight="600" font-size="14" fill="var(--plum)">BRIGHTVALE</text>
  </g>

  <!-- Slide: closing -->
  <g class="slide">
    <rect x="784" y="1023" width="664" height="374" fill="var(--lilac)"/>
    <ellipse cx="1300" cy="1330" rx="130" ry="55" fill="var(--lilac-soft)" opacity="0.6" role="img" aria-label="Faint galloping horse silhouette decoration"/>
    <circle cx="1042" cy="1118" r="33" fill="var(--white)"/>
    <text x="1087" y="1112" font-family="'Roboto Slab', serif" font-weight="400" font-size="15" fill="var(--white)">THE COPPER LANTERN</text>
    <text x="1087" y="1132" font-family="'Roboto Slab', serif" font-weight="400" font-size="15" fill="var(--white)">ADVISORY GROUP</text>
    <text class="display" x="1115" y="1245" font-size="50" fill="var(--white)" text-anchor="middle" font-weight="800">THANK YOU!</text>
    <text class="display-light" x="1115" y="1285" font-size="41" fill="var(--white)" text-anchor="middle">FOR WATCHING</text>
  </g>
</svg>
</body>
</html>
```